Easy Re-Design for Hot Chicken and Food Bags

We are a medium sized Deli and Butchery looking to do our own print on our Roast Chicken and Hot Food bags. I am looking for 2 designs:
1 x Roast Chicken Bag
1 x Hot Food Bag for all other hot items
I would like them to look modern and easy to read. Same theme but different so its easy to determine. The less colours used, the better. And only the Roast Chicken Bag needs an ingredients section for the stuffing (to be confirmed) and a barcode.
We attempted the Graphics on this but we are after a professional to make it look as appealing as possible, so we sell as many as possible. : )
Middle Income Families

```html
<!DOCTYPE html>
<html lang="en">
<head>
<meta charset="utf-8">
<title>Ember Hall – Hot Food Bags</title>
<link rel="stylesheet" href="https://fonts.googleapis.com/css2?family=Bebas+Neue&family=Oswald:wght@600&display=swap">
<style>
  :root {
    --red: #c0091a;
    --black: #0b0b0b;
    --white: #ffffff;
    --ink: #3a3a3a;
    --flame-deep: #5a1a04;
    --flame-mid: #d9650f;
    --flame-light: #f7c14a;
  }
  * { box-sizing: border-box; margin: 0; padding: 0; }
  html, body { width: 1200px; height: 1000px; overflow: hidden; background: var(--white); }
  .canvas { position: relative; width: 1200px; height: 1000px; background: var(--white); }

  /* header brand */
  .brand-rule { position: absolute; top: 140px; height: 3px; background: var(--red); }
  .brand-rule--left { left: 70px; width: 400px; }
  .brand-rule--right { left: 746px; width: 400px; }
  .brand-name {
    position: absolute; left: 500px; top: 62px; width: 200px;
    text-align: center; font-family: "Oswald", sans-serif; font-weight: 600;
    font-size: 64px; line-height: 0.95; color: var(--red);
  }

  /* bag */
  .bag { position: absolute; top: 260px; width: 398px; height: 660px; }
  .bag--chicken { left: 200px; }
  .bag--hotfood { left: 632px; }

  .half { position: absolute; left: 0; width: 398px; height: 330px; }
  .half--top { top: 0; }
  .half--bottom { top: 330px; transform: rotate(180deg); }

  .band { position: absolute; left: 0; top: 0; width: 398px; height: 90px; background: var(--red); border-radius: 6px 6px 0 0; }
  .panel { position: absolute; left: 0; top: 90px; width: 398px; height: 170px; background: var(--black); overflow: hidden; }
  .flames {
    position: absolute; left: 0; bottom: 0; width: 100%; height: 100px;
    background: linear-gradient(to top, var(--flame-deep) 0%, var(--flame-mid) 35%, var(--flame-light) 60%, rgba(217,101,15,0.4) 80%, rgba(11,11,11,0) 100%);
  }

  .logo-tab {
    position: absolute; left: 149px; top: 0; width: 100px; height: 100px;
    background: var(--white); border-radius: 0 0 12px 12px;
    display: flex; align-items: center; justify-content: center; text-align: center;
    font-family: "Oswald", sans-serif; font-weight: 600; font-size: 24px; line-height: 1;
    color: var(--red); z-index: 2;
  }

  .title {
    position: absolute; left: 0; width: 100%; text-align: center;
    font-family: "Bebas Neue", sans-serif; color: var(--white);
    text-shadow: 3px 3px 0 #6d6d6d;
  }
  .title--kicker { top: 110px; font-size: 36px; letter-spacing: 1px; }
  .title--main { top: 144px; font-size: 72px; letter-spacing: 2px; }
  .title--hot { top: 118px; font-size: 78px; letter-spacing: 3px; }
  .dot { display: inline-block; width: 8px; height: 8px; background: var(--white); vertical-align: middle; margin: 0 10px; box-shadow: 1px 1px 0 #6d6d6d; }

  .gusset { position: absolute; left: 0; top: 260px; width: 398px; height: 70px; }
  .gusset svg { position: absolute; inset: 0; }
  .gusset-label {
    position: absolute; left: 0; top: 18px; width: 100%; text-align: center;
    font-family: "Bebas Neue", sans-serif; font-size: 27px; color: var(--white);
    text-shadow: 2px 2px 0 #6e0610; letter-spacing: 0.5px;
  }

  .ingredients { position: absolute; left: 78px; top: 6px; width: 242px; color: var(--white); }
  .ingredients-heading {
    font-family: "Bebas Neue", sans-serif; font-size: 11px; text-align: center; letter-spacing: 0.5px;
  }
  .ingredients-box {
    border: 1px solid var(--white); padding: 3px 5px; margin-top: 2px;
    font-family: "Oswald", sans-serif; font-weight: 600; font-size: 5.6px; line-height: 1.35;
  }
</style>
</head>
<body>
<main class="canvas">
  <div class="brand-rule brand-rule--left"></div>
  <div class="brand-name">EMBER<br>HALL</div>
  <div class="brand-rule brand-rule--right"></div>

  <!-- Roast chicken bag -->
  <section class="bag bag--chicken">
    <div class="half half--top">
      <div class="band"></div>
      <div class="logo-tab">EMBER<br>HALL</div>
      <div class="panel"><div class="flames" role="img" aria-label="Photo of roaring grill flames"></div></div>
      <div class="title title--kicker">WHOLE ROASTED</div>
      <div class="title title--main"><span class="dot"></span>CHICKEN<span class="dot"></span></div>
      <div class="gusset">
        <svg width="398" height="70" viewBox="0 0 398 70"><polygon points="0,0 398,0 358,70 40,70" fill="#c0091a"/></svg>
        <div class="gusset-label"><span class="dot"></span>WHOLE ROASTED CHICKEN<span class="dot"></span></div>
      </div>
    </div>
    <div class="half half--bottom">
      <div class="band"></div>
      <div class="logo-tab">EMBER<br>HALL</div>
      <div class="panel"><div class="flames" role="img" aria-label="Photo of roaring grill flames"></div></div>
      <div class="title title--kicker">WHOLE ROASTED</div>
      <div class="title title--main"><span class="dot"></span>CHICKEN<span class="dot"></span></div>
      <div class="gusset">
        <svg width="398" height="70" viewBox="0 0 398 70"><polygon points="0,0 398,0 358,70 40,70" fill="#c0091a"/></svg>
        <div class="gusset-label"><span class="dot"></span>WHOLE ROASTED CHICKEN<span class="dot"></span></div>
      </div>
    </div>
  </section>

  <!-- Hot food bag -->
  <section class="bag bag--hotfood">
    <div class="half half--top">
      <div class="band"></div>
      <div class="logo-tab">EMBER<br>HALL</div>
      <div class="panel"><div class="flames" role="img" aria-label="Photo of roaring grill flames"></div></div>
      <div class="title title--hot"><span class="dot"></span>HOT FOOD<span class="dot"></span></div>
      <div class="gusset">
        <svg width="398" height="70" viewBox="0 0 398 70"><polygon points="0,0 398,0 358,70 40,70" fill="#c0091a"/></svg>
        <div class="gusset-label"><span class="dot"></span>WHOLE ROASTED CHICKEN<span class="dot"></span></div>
      </div>
    </div>
    <div class="half half--bottom">
      <div class="band"></div>
      <div class="logo-tab">EMBER<br>HALL</div>
      <div class="panel"><div class="flames" role="img" aria-label="Photo of roaring grill flames"></div></div>
      <div class="title title--hot"><span class="dot"></span>HOT FOOD<span class="dot"></span></div>
      <div class="gusset">
        <svg width="398" height="70" viewBox="0 0 398 70"><polygon points="0,0 398,0 358,70 40,70" fill="#c0091a"/></svg>
        <div class="ingredients">
          <div class="ingredients-heading">INGREDIENTS</div>
          <div class="ingredients-box">Stuffing ingredients to be confirmed. Breadcrumbs, onion, butter, sage, parsley, thyme, salt, black pepper, lemon zest, garlic and free range egg. Contains gluten, egg and milk. Prepared in a kitchen that also handles nuts, sesame and mustard. Keep hot and eat within two hours.</div>
        </div>
      </div>
    </div>
  </section>
</main>
</body>
</html>
```